New Web-Page Design Required

We need a new or initial web design for our page vorlan-grid.com. We provide products & services around infrastructure products. We have two products at the moment, but another 2 in the pipeline.
We want to have the following page structure (and part of the project is to design the 7 pages):
- Home
- Products
-One page per product
- Service
- Support
- About
- Contact (Email form)
The start page should include the following information:
- Twitter / Linkedin Links
- Telephone / Email or in general contact details
- News
- Maybe a link-box, where we can highlight/showcase things
- Link to our support portal, quite prominent
- Testimonials
It would be nice if the product pages would have a image header, where we can put up a screenshot or something. Links to datasheet and videos of the product would be nice as well.
We like the "big banner in the middle" designs, like these two Joomla examples. No need to copy them, it should just give you an idea.
http://www.pelmorthemes.com/itempreview/185
http://www.pelmorthemes.com/content/asj42/index.php
Budget for images available, so please use placeholders or ask us for specific photos/images, if you need them for your design.
Target Market(s)
Business-2-Business, Decision makers and Technical Leads
Industry/Entity Type
News
Look and feel

```html
<!DOCTYPE html>
<html lang="en">
<head>
<meta charset="utf-8">
<title>vorlan·grid — Home</title>
<link rel="stylesheet" href="https://fonts.googleapis.com/css2?family=Handlee&family=Open+Sans:wght@400;600&display=swap">
<style>
  :root {
    --teal: #0b7889;
    --teal-dark: #086372;
    --text: #333333;
    --grey-ring: #444444;
    --white: #ffffff;
    --green-top: #a6d95a;
    --green-bottom: #7cbf2e;
    --orange-top: #f7b81c;
    --orange-bottom: #eb9a05;
  }
  * { margin: 0; padding: 0; box-sizing: border-box; }
  html, body { width: 1200px; height: 1072px; overflow: hidden; background: var(--white); }
  body { position: relative; font-family: "Open Sans", Arial, sans-serif; color: var(--text); }

  .site-header { position: absolute; left: 0; top: 0; width: 1200px; height: 104px; background: var(--white); }
  .brand { position: absolute; left: 120px; top: 25px; display: flex; align-items: center; gap: 10px; }
  .brand-mark { width: 52px; height: 52px; border-radius: 50%; background: var(--teal); }
  .brand-name { font-size: 36px; font-weight: 600; color: #555555; letter-spacing: -0.5px; }

  .main-nav { position: absolute; top: 0; left: 516px; height: 104px; display: flex; }
  .main-nav a { display: block; height: 102px; line-height: 120px; font-size: 14px; color: var(--text); text-decoration: none; padding: 0 22px; }
  .main-nav a.is-active { color: var(--teal); border-bottom: 4px solid var(--teal); box-shadow: 0 -2px 6px rgba(0,0,0,0.06); }
  .main-nav a + a { margin-left: 9px; }

  .hero-photo { position: absolute; left: 0; top: 104px; width: 1200px; height: 481px;
    background: linear-gradient(180deg, #2f5f86 0%, #5e8fb5 45%, #4b7390 75%, #8aa3b3 100%); }
  .hero-fade { position: absolute; left: 0; top: 585px; width: 1200px; height: 90px;
    background: linear-gradient(180deg, #eef1f3 0%, #ffffff 100%); }
  .device-showcase { position: absolute; left: 146px; top: 216px; width: 900px; height: 412px;
    border-radius: 10px; background: linear-gradient(135deg, #e8e8e8 0%, #e8e8e8 31%, #262a2e 31%, #1b1e21 100%);
    box-shadow: 0 14px 30px rgba(0,0,0,0.35); }

  .tagline { position: absolute; left: 190px; top: 674px; width: 820px; text-align: center;
    font-family: "Handlee", cursive; font-size: 19px; line-height: 24px; color: var(--teal); }

  .cta { position: absolute; top: 744px; height: 44px; border-radius: 3px; display: flex; align-items: center;
    justify-content: center; gap: 8px; font-size: 14px; color: #333333; text-decoration: none; }
  .cta svg { width: 18px; height: 18px; }
  .cta-video { left: 396px; width: 201px; background: linear-gradient(180deg, var(--green-top), var(--green-bottom)); border: 1px solid #74b226; }
  .cta-datasheet { left: 605px; width: 201px; background: linear-gradient(180deg, var(--orange-top), var(--orange-bottom)); border: 1px solid #d98c00; }

  .feature { position: absolute; top: 851px; width: 166px; text-align: center; text-decoration: none; }
  .feature svg { width: 166px; height: 166px; display: block; }
  .feature-label { display: block; margin-top: 16px; font-size: 16px; color: var(--teal); }
  .feature-products { left: 153px; }
  .feature-service { left: 516px; }
  .feature-support { left: 880px; }
</style>
</head>
<body>
  <header class="site-header">
    <div class="brand"><span class="brand-mark"></span><span class="brand-name">vorlan·grid</span></div>
    <nav class="main-nav">
      <a class="is-active" href="#">Home</a>
      <a href="#">Products</a>
      <a href="#">Service</a>
      <a href="#">Support</a>
      <a href="#">About</a>
      <a href="#">Contact</a>
    </nav>
  </header>

  <div class="hero-photo" role="img" aria-label="Blurred photograph of a bright modern office interior"></div>
  <div class="hero-fade"></div>
  <div class="device-showcase" role="img" aria-label="Product screenshots shown on a tablet, a desktop window and a smartphone, displaying network monitoring dashboards"></div>

  <p class="tagline">Quisque sed orci a nunc vehicula dapibus nec ac augue. Aliquam iaculis tristique diam, vel fac-<br>ilisis velit volutpat et. Aenean at leo sit amet purus Curabitur sit amet nulla vitae</p>

  <a class="cta cta-video" href="#">
    <svg viewBox="0 0 18 18"><path d="M1 9c2.5-4 5-5 8-5s5.5 1 8 5c-2.5 4-5 5-8 5s-5.5-1-8-5z" fill="none" stroke="#333" stroke-width="1.6"/><circle cx="9" cy="9" r="2.6" fill="#333"/></svg>
    Watch the video
  </a>
  <a class="cta cta-datasheet" href="#">
    <svg viewBox="0 0 18 18"><path d="M9 2v9M5 7l4 4 4-4" fill="none" stroke="#333" stroke-width="1.8"/><path d="M2 12v4h14v-4" fill="none" stroke="#333" stroke-width="1.8"/></svg>
    Download Datasheet
  </a>

  <a class="feature feature-products" href="#">
    <svg viewBox="0 0 166 166"><circle cx="83" cy="83" r="80" fill="none" stroke="var(--teal)" stroke-width="5"/><circle cx="83" cy="83" r="71" fill="var(--teal)"/>
      <path d="M68 68L54 84l14 16M98 68l14 16-14 16" fill="none" stroke="#fff" stroke-width="7" stroke-linecap="square"/><path d="M89 62L77 106" stroke="#fff" stroke-width="6"/></svg>
    <span class="feature-label">Products</span>
  </a>
  <a class="feature feature-service" href="#">
    <svg viewBox="0 0 166 166"><circle cx="83" cy="83" r="80" fill="none" stroke="var(--grey-ring)" stroke-width="5"/><circle cx="83" cy="83" r="71" fill="var(--teal)"/>
      <g transform="translate(79 80)"><circle r="15" fill="none" stroke="#fff" stroke-width="9" stroke-dasharray="6 5.8"/><circle r="12" fill="none" stroke="#fff" stroke-width="6"/></g>
      <g transform="translate(101 109)"><circle r="8" fill="none" stroke="#fff" stroke-width="5" stroke-dasharray="3.5 2.8"/><circle r="6" fill="none" stroke="#fff" stroke-width="3.5"/></g></svg>
    <span class="feature-label">Service</span>
  </a>
  <a class="feature feature-support" href="#">
    <svg viewBox="0 0 166 166"><circle cx="83" cy="83" r="80" fill="none" stroke="var(--teal)" stroke-width="5"/><circle cx="83" cy="83" r="71" fill="var(--teal)"/>
      <circle cx="83" cy="76" r="14" fill="#fff"/><path d="M67 76a16 16 0 0 1 32 0" fill="none" stroke="#fff" stroke-width="4"/>
      <path d="M58 110c2-13 12-18 25-18s23 5 25 18z" fill="#fff"/></svg>
    <span class="feature-label">Support</span>
  </a>
</body>
</html>
```